High End Mechanic Business Card Design Project

Automotive Business - Repair, service and sales
Bold background with clarity of text

Industry/Entity Type

Automotive

Contact Information for Business Card

Black background with silver or white valdorn 482 range coupe at the bottom right angered with the business name and address at the top left.. Also to include a compass near the business name and the text... Sales Service RepairAdded photos as EXAMPLES. Don't want the actual n, s, e w on the compass picture but to know that it is a compass.

Font styles to use
Sans Serif

Requirements
Must have
• Creativity, black background, Images: 4 Range Valdorn Coupe & Compass (without text)

```html
<!DOCTYPE html>
<html lang="en">
<head>
<meta charset="utf-8">
<title>Harrowgate East Motors – Business Card</title>
<link rel="stylesheet" href="https://fonts.googleapis.com/css2?family=Roboto+Slab:wght@300;400;500&display=block">
<style>
  :root {
    --ink-black: #050607;
    --panel-dark: #1c1e21;
    --panel-mid: #2b2e32;
    --brand-blue: #2a8bbf;
    --banner-blue: #1f7db3;
    --banner-deep: #0f5f8e;
    --emblem-grey: #3a3b3d;
    --emblem-blue: #1a86bf;
    --text-white: #ffffff;
    --car-light: #e9ecef;
    --car-shadow: #9aa1a8;
  }
  * { margin: 0; padding: 0; box-sizing: border-box; }
  html, body {
    width: 1200px; height: 690px; overflow: hidden;
    background: var(--ink-black);
  }
  .card {
    position: relative;
    width: 1200px; height: 690px;
    overflow: hidden;
    background:
      radial-gradient(ellipse 60% 55% at 50% 45%, var(--panel-mid) 0%, var(--panel-dark) 45%, var(--ink-black) 100%);
    font-family: "Roboto Slab", "Rockwell", "Zilla Slab", serif;
  }
  .business-name {
    position: absolute;
    top: 58px; left: 0; width: 1200px;
    text-align: center;
    font-family: "Roboto Slab", "Rockwell", serif;
    font-weight: 500;
    font-size: 94px;
    letter-spacing: 0.5px;
    color: var(--brand-blue);
    line-height: 1.1;
    white-space: nowrap;
  }
  .compass-emblem {
    position: absolute;
    left: 49px; top: 195px;
    width: 272px; height: 272px;
    border-radius: 50%;
    background: radial-gradient(circle at 50% 50%, var(--emblem-blue) 0%, var(--emblem-grey) 38%, #2a2b2d 100%);
  }
  .contact {
    position: absolute;
    left: 300px; top: 207px; width: 666px;
    text-align: center;
    font-family: "Roboto Slab", "Rockwell", serif;
    font-weight: 300;
    font-size: 50px;
    color: var(--text-white);
    line-height: 75px;
    font-style: normal;
    white-space: nowrap;
  }
  .services-banner {
    position: absolute;
    left: 0; top: 554px;
    width: 644px; height: 76px;
  }
  .services-banner svg { position: absolute; inset: 0; }
  .services-text {
    position: absolute;
    left: 32px; top: 0; height: 76px;
    display: flex; align-items: center;
    font-family: "Roboto Slab", "Rockwell", serif;
    font-weight: 400;
    font-size: 50px;
    color: var(--text-white);
    white-space: nowrap;
  }
  .car-photo {
    position: absolute;
    left: 697px; top: 429px;
    width: 471px; height: 227px;
    border-radius: 110px 140px 40px 60px;
    background: linear-gradient(160deg, var(--car-light) 0%, #cfd4d9 55%, var(--car-shadow) 100%);
  }
</style>
</head>
<body>
  <main class="card">
    <h1 class="business-name">Harrowgate East Motors</h1>

    <div class="compass-emblem" role="img" aria-label="Compass emblem with a blue needle, no direction letters"></div>

    <address class="contact">
      <div class="contact-street">2750 Linwood Ridge Blvd,</div>
      <div class="contact-city">Dorrance, GA 31290</div>
      <div class="contact-phone">Tel. 555.419.0274</div>
    </address>

    <div class="services-banner">
      <svg viewBox="0 0 644 76" preserveAspectRatio="none" aria-hidden="true">
        <defs>
          <linearGradient id="bannerFill" x1="0" y1="0" x2="0" y2="1">
            <stop offset="0" stop-color="var(--banner-blue)"/>
            <stop offset="1" stop-color="var(--banner-deep)"/>
          </linearGradient>
        </defs>
        <polygon points="0,0 644,0 592,76 0,76" fill="url(#bannerFill)"/>
      </svg>
      <p class="services-text">Sales - Service - Repair</p>
    </div>

    <div class="car-photo" role="img" aria-label="Photo of a white 4 Range Valdorn Coupe, front three-quarter view"></div>
  </main>
</body>
</html>
```